Larkspur Homes - wanted BRILLIANT website design for our new property investing company

We need a website design for our new company based in Bristol, England, UK called "Larkspur Homes". We help buy people property who are in financial difficulty or who are needing to sell their property quickly for reasons such as death, divorce/separation, relocation, emigration.

We have a logo being designed incorporating strawberry and property (so red and green). We would like designs to communicate an elegant ,professional, approachable, friendly
fresh clean but also warm appealing appearance
Not too busy
Website consistent with logo and company name i.e. colour scheme

Please use our word document for content as a guide but use professional judgement for minor alterations if you feel they would benefit the site/structure etc

Please ask at any time if not sure

Target Market(s)

Adult british population, those that have a mortgage / loan / own property

Industry/Entity Type

Financial

Font styles to use
Serif
Sans Serif
Decorative

Colors
0692cd
33b7a4
acd036
fbee3e
3176b5
886aae
a6479a
e567a6
eb1f27

Requirements
Must have
• This must not look like a template website we are looking for UNIQUE please!
Nice to have
• Bristol pictures instead of generic, or colourful line drawings/comic drawings of houses/property/keys/happy people.....
Should not have
• An obvious off the shelf template design

```html
<!DOCTYPE html>
<html lang="en">
<head>
<meta charset="utf-8">
<title>Larkspur Homes</title>
<link rel="stylesheet" href="https://fonts.googleapis.com/css2?family=Roboto+Condensed:wght@400;700&family=Marcellus&family=Poppins:wght@200&family=Arimo:wght@400;700&display=swap">
<style>
:root{
  --red:#d9252a;
  --dark:#232b2b;
  --slate:#2e3e3f;
  --green:#4db72b;
  --page:#f5f5f5;
  --panel:#e8e8e8;
  --panel-line:#cfcfcf;
  --footer:#181818;
  --ink:#111;
  --white:#fff;
}
*{box-sizing:border-box;margin:0;padding:0}
html,body{width:746px;height:1200px;overflow:hidden}
body{position:relative;background:var(--page);font-family:Arimo,Arial,sans-serif;color:var(--ink)}
.abs{position:absolute}

/* header */
.top-strip{left:0;top:0;width:746px;height:5px;background:var(--dark)}
.brand-bar{left:0;top:5px;width:746px;height:52px;background:var(--red)}
.tab{top:5px;height:18px;background:var(--dark);color:var(--white);display:flex;align-items:center;gap:6px;padding:0 8px}
.tab-email{left:113px;width:134px;font-size:7.5px}
.tab-phone{left:518px;width:118px;font-size:12.5px;font-weight:700;justify-content:center}
.site-name{left:0;top:24px;width:746px;text-align:center;color:var(--white);font-family:"Roboto Condensed",sans-serif;font-weight:700;font-size:19px}
.main-nav{left:0;top:57px;width:746px;height:39px;background:var(--dark);display:flex;justify-content:center;gap:23px;padding-top:15px}
.main-nav a{color:var(--white);text-decoration:none;font-size:7.3px;height:14px;padding:0 1px}
.main-nav a.current{border-bottom:1px solid var(--red);padding:0 4px}

/* hero */
.hero{left:0;top:96px;width:746px;height:254px;background:linear-gradient(180deg,#8ea3b5 0%,#b7c0c3 35%,#8b8472 65%,#4e4a40 100%)}
.hero-welcome{left:117px;top:130px;font-family:Poppins,sans-serif;font-weight:200;font-size:33px;color:#111;letter-spacing:.5px}
.hero-name{left:117px;top:164px;font-family:"Roboto Condensed",sans-serif;font-weight:700;font-size:37px;color:var(--red);letter-spacing:1px}
.hero-caption{left:117px;top:209px;width:264px;height:45px;background:rgba(40,52,52,.9);color:var(--white);font-size:15.5px;line-height:18px;padding:4px 6px}
.slider-arrow{top:321px;width:30px;height:29px;background:var(--green);display:flex;align-items:center;justify-content:center}
.slider-prev{left:510px}.slider-next{left:542px}

/* welcome */
.welcome-title{left:0;top:366px;width:746px;text-align:center;font-family:Marcellus,serif;font-size:25px;color:var(--green)}
.welcome-text{left:122px;top:401px;width:502px;font-size:9.3px;line-height:15px;text-align:justify;text-align-last:center}

/* services */
.services-title{left:127px;top:512px;width:300px;font-size:14.5px;font-weight:700;line-height:19px}
.services-lead{left:127px;top:554px;font-size:9.5px;color:var(--green)}
.services-list{left:127px;top:574px;list-style:none;font-size:8.3px;line-height:14.8px}
.services-list li::before{content:"• "}

/* panels */
.panel{background:var(--panel);border:1px solid var(--panel-line);border-radius:3px;overflow:hidden}
.panel-head{background:var(--red);color:var(--white);font-family:"Roboto Condensed",sans-serif;font-weight:700;padding-left:11px}
.contact-panel{left:117px;top:725px;width:316px;height:256px}
.contact-panel .panel-head{height:28px;font-size:15px;line-height:30px}
.field-label{width:84px;text-align:right;font-size:8.3px}
.field{left:210px;width:189px;height:19px;background:var(--slate)}
.btn{background:var(--green);color:var(--white);font-size:8.3px;font-weight:700;border-radius:2px;display:flex;align-items:center;justify-content:center;height:16px}

.help-panel{left:462px;top:501px;width:167px;height:480px}
.help-panel .panel-head{height:34px;font-size:14px;line-height:39px;letter-spacing:.3px}
.help-link{left:470px;width:151px;height:20px;background:var(--slate);color:var(--white);font-family:"Roboto Condensed",sans-serif;font-size:8px;line-height:20px;padding-left:6px;border:1px solid #1d2828}

/* footer */
.footer-bar{left:0;top:1037px;width:746px;height:25px;background:var(--red);display:flex;gap:32px;padding:9px 0 0 122px}
.footer-bar a{color:var(--white);font-size:7px;text-decoration:none}
.footer{left:0;top:1062px;width:746px;height:138px;background:var(--footer);color:var(--white)}
.footer-name{left:122px;top:1090px;font-family:"Roboto Condensed",sans-serif;font-weight:700;font-size:13px}
.footer-memberships{left:122px;top:1113px;font-size:7.2px;line-height:11px}
.follow{left:122px;top:1158px;font-size:7.5px}
.social{top:1153px;width:18px;height:18px;border-radius:3px}
.social-a{left:175px;background:#3b5998}
.social-b{left:195px;background:#4fb6e6}
.map{left:298px;top:1077px;width:164px;height:101px;background:linear-gradient(135deg,#e8e4d8,#f3efe4 50%,#dcd6c6)}
.footer-contact{left:430px;top:1088px;width:195px;text-align:right}
.footer-contact h3{font-family:"Roboto Condensed",sans-serif;font-size:13px;color:var(--green);margin-bottom:3px}
.footer-contact p{font-size:8.8px;line-height:11.3px}
</style>
</head>
<body>

<div class="abs top-strip"></div>
<header>
  <div class="abs brand-bar"></div>
  <div class="abs tab tab-email">
    <svg width="9" height="7" viewBox="0 0 9 7"><rect x=".5" y=".5" width="8" height="6" fill="none" stroke="#fff"/><path d="M.5 .5 4.5 4 8.5 .5" fill="none" stroke="#fff"/></svg>
    info@larkspur-homes.co.uk
  </div>
  <div class="abs tab tab-phone">
    <svg width="9" height="9" viewBox="0 0 24 24"><path fill="#fff" d="M6.6 10.8a15 15 0 0 0 6.6 6.6l2.2-2.2c.3-.3.7-.4 1-.2 1.1.4 2.3.6 3.6.6.6 0 1 .4 1 1V20c0 .6-.4 1-1 1A17 17 0 0 1 3 4c0-.6.4-1 1-1h3.5c.6 0 1 .4 1 1 0 1.3.2 2.5.6 3.6.1.3 0 .7-.2 1z"/></svg>
    07700900461
  </div>
  <div class="abs site-name">LARKSPUR HOMES</div>
  <nav class="abs main-nav">
    <a class="current">Home</a>
    <a>Sell Your Property Fast</a>
    <a>Rent Your Property Fast</a>
    <a>Common Questions</a>
    <a>About Us</a>
    <a>Contact Us</a>
  </nav>
</header>

<section>
  <div class="abs hero" role="img" aria-label="Photograph of a city skyline with tall office towers under a cloudy sky"></div>
  <h1 class="abs hero-welcome">WELCOME TO</h1>
  <div class="abs hero-name">LARKSPUR HOMES</div>
  <p class="abs hero-caption">Lorem ipsum dolor sit amet, consectetur adipisicing elit, sed do eiusmod tempor</p>
  <div class="abs slider-arrow slider-prev"><svg width="14" height="16" viewBox="0 0 14 16"><path d="M12 1 2 8l10 7" fill="none" stroke="#fff" stroke-width="1.2"/></svg></div>
  <div class="abs slider-arrow slider-next"><svg width="14" height="16" viewBox="0 0 14 16"><path d="M2 1l10 7-10 7" fill="none" stroke="#fff" stroke-width="1.2"/></svg></div>
</section>

<section>
  <h2 class="abs welcome-title">WELCOME</h2>
  <p class="abs welcome-text">Lorem ipsum dolor sit amet, consectetur adipisicing elit, sed do eiusmod tempor incididunt ut labore et dolore magna aliqua. Ut enim ad minim veniam, quis nostrud exercitation ullamco laboris nisi ut aliquip ex ea commodo consequat. Duis aute irure dolor in reprehenderit in voluptate velit esse cillum dolore eu fugiat nulla pariatur. Excepteur sint occaecat cupidatat non proident, sunt in culpa qui officia deserunt mollit anim id est laborum.</p>
</section>

<section>
  <h2 class="abs services-title">Do you want to sell or rent out your house quickly?</h2>
  <p class="abs services-lead">We are a local family run property business who specialize in</p>
  <ul class="abs services-list">
    <li>Buying properties quickly</li>
    <li>Finding creative solutions to your property problems</li>
    <li>Property rental management</li>
    <li>Lettings to professional and student tenants</li>
    <li>Guaranteed rent and management schemes for landlords</li>
    <li>STOPPING repossessions</li>
    <li>Motivated sellers</li>
    <li>Chain fixing</li>
    <li>Negative equity problems</li>
  </ul>
</section>

<section>
  <div class="abs panel contact-panel"><div class="panel-head">CONTACT FORM</div></div>
  <div class="abs field-label" style="left:117px;top:763px">Your Name:</div>
  <div class="abs field" style="top:763px"></div>
  <div class="abs field-label" style="left:117px;top:790px">Email Address:</div>
  <div class="abs field" style="top:791px"></div>
  <div class="abs field-label" style="left:117px;top:817px">Phone Number:</div>
  <div class="abs field" style="top:818px"></div>
  <div class="abs field-label" style="left:117px;top:844px">Property Address:</div>
  <div class="abs field" style="top:845px"></div>
  <div class="abs field-label" style="left:117px;top:870px">Message:</div>
  <div class="abs field" style="top:871px;height:66px"></div>
  <div class="abs btn" style="left:210px;top:947px;width:41px">SUBMIT</div>
</section>

<aside>
  <div class="abs panel help-panel"><div class="panel-head">WHO CAN WE HELP?</div></div>
  <div class="abs help-link" style="top:549px">HOW TO STOP REPOSSESSION</div>
  <div class="abs help-link" style="top:577px">DIVORCE OR SEPARATION</div>
  <div class="abs help-link" style="top:604px">FINANCIAL PROBLEMS</div>
  <div class="abs help-link" style="top:632px">DON'T LIKE ESTATE AGENTS?</div>
  <div class="abs help-link" style="top:660px">PROPERTY NEEDING WORK</div>
  <div class="abs help-link" style="top:687px">RETIRING LANDLORDS</div>
  <div class="abs help-link" style="top:716px">NEGATIVE EQUITY</div>
  <div class="abs help-link" style="top:743px">OPPORTUNITY NOT TO BE MISSED!!</div>
  <div class="abs help-link" style="top:771px">GUARANTEED RENT SCHEME</div>
  <div class="abs help-link" style="top:800px">ILL HEALTH</div>
  <div class="abs help-link" style="top:827px">RELOCATING</div>
  <div class="abs help-link" style="top:854px">INHERITED PROPERTY</div>
  <div class="abs help-link" style="top:883px">CHAIN COLLAPSE</div>
  <div class="abs help-link" style="top:911px">TENANTED PROPERTY</div>
  <div class="abs btn" style="left:470px;top:944px;width:41px">SUBMIT</div>
</aside>

<footer>
  <nav class="abs footer-bar"><a>About Us</a><a>Contact Us</a></nav>
  <div class="abs footer"></div>
  <div class="abs footer-name">LARKSPUR HOMES</div>
  <p class="abs footer-memberships">GCSA (Guild of Certified Surveying Associates),<br>LFA (Landlord Fellowship Alliance),<br>The Housing Fair Practice Panel</p>
  <div class="abs follow">FOLLOW US:</div>
  <div class="abs social social-a" aria-label="Social profile one"></div>
  <div class="abs social social-b" aria-label="Social profile two"></div>
  <div class="abs map" role="img" aria-label="Street map showing the office location"></div>
  <div class="abs footer-contact">
    <h3>CONTACT US</h3>
    <p>2014 Larkspur Homes Limited.<br>Reg No 7734210<br>07700900461<br>info@larkspur-homes.co.uk</p>
  </div>
</footer>

</body>
</html>
```